Website Layout for PanFolio

PanFolio is a company that will be dedicated (for now) to publishing recipes with the nutrition facts. Run by a nutritionist. In the future there may be a mobile app.

We need layout for 3 of the pages of the website. NO PROGRAMMING, only layout and graphic design. Not very complicated.

--Please view the details in the attached document--
We want a layout design for the pages: P.01, P.02 and P.03

Logo is also attached. Please don't hesitate if you want to modify the logo to fit your idea. The design should be clean, visually attractive and refreshing to look at. It should be sleek and a feel of technology, yet also natural and culinary.

Some examples to get ideas:

http://www.marlowhearthtales.com/
http://www.tavelbrunefare.org/site/
http://thecobaltladle.com/products/dice-deck
Updates

Project Deadline Extended
Reason: I extend the deadline for this week to allow you space for work on the observations made to your design and to provide the P.02 and P.03 designs. We greatly appreciate your hard work and are thrilled with your ideas.

Target Market(s)

Young people that live alone or want to optimize their cooking.
Young, modern housewives with a smartphone.

Industry/Entity Type

Nutrition

Requirements
Must have
• --Please view the details in the attached document--
NO PROGRAMMING. Only layout and graphic design.

```html
<!DOCTYPE html>
<html lang="en">
<head>
<meta charset="utf-8">
<title>PanFolio</title>
<link rel="stylesheet" href="https://fonts.googleapis.com/css2?family=Tinos:wght@400;700&display=swap">
<style>
  :root {
    --page-bg: #f0f0f0;
    --page-line: rgba(0,0,0,0.025);
    --column-bg: #fdfdfd;
    --band-bg: #e5e5e5;
    --band-edge: #dedede;
    --ink: #111111;
    --brand-ink: #3a3a3a;
    --icon-grey: #a3a3a3;
    --accent: #e2603c;
    --search-border: #e4e4e4;
    --photo-left-dark: #3b1814;
    --photo-left-mid: #8a4a22;
    --photo-left-warm: #d69a3e;
    --photo-left-plate: #ece6de;
    --photo-right-dark: #2f1e12;
    --photo-right-mid: #8a6038;
    --photo-right-warm: #d9b27a;
    --photo-right-plate: #efe3cc;
  }
  * { margin: 0; padding: 0; box-sizing: border-box; }
  html, body { width: 1200px; height: 1000px; overflow: hidden; }
  body {
    position: relative;
    background-color: var(--page-bg);
    background-image:
      repeating-linear-gradient(0deg, var(--page-line) 0 1px, transparent 1px 4px),
      repeating-linear-gradient(90deg, var(--page-line) 0 1px, transparent 1px 4px);
    font-family: "Tinos", "Times New Roman", serif;
    color: var(--ink);
  }
  .column {
    position: absolute; left: 223px; top: 0; width: 757px; height: 1000px;
    background: var(--column-bg);
    box-shadow: 0 0 20px rgba(0,0,0,0.07);
  }

  .social { position: absolute; left: 839px; top: 27px; display: flex; gap: 11px; }
  .social span { width: 17px; height: 17px; border-radius: 50%; background: var(--icon-grey); }

  .brand {
    position: absolute; left: 292px; top: 50px;
    display: flex; align-items: center; gap: 26px;
  }
  .brand-mark {
    width: 160px; height: 160px; border-radius: 16px;
    background: var(--accent);
    box-shadow: 0 14px 14px -10px rgba(40,40,80,0.25);
  }
  .brand-name {
    font-size: 84px; font-weight: 700; color: var(--brand-ink);
    letter-spacing: -0.5px; margin-top: 40px;
  }

  .nav { list-style: none; font-size: 12px; letter-spacing: 1.6px; }
  .nav li {
    position: absolute; top: 277px;
    border-bottom: 1px solid var(--ink); line-height: 14px;
  }
  .nav .home { left: 302px; }
  .nav .about { left: 378px; }
  .nav .contact { left: 458px; }
  .nav .login { left: 557px; }
  .nav .logout { left: 632px; top: 278px; }

  .search {
    position: absolute; left: 731px; top: 276px; width: 220px; height: 25px;
    border: 1px solid var(--search-border); border-radius: 12px; background: #fff;
    box-shadow: inset 0 2px 3px rgba(0,0,0,0.07);
  }
  .search svg { position: absolute; right: 14px; top: 2px; }

  .intro-band {
    position: absolute; left: 0; top: 326px; width: 1200px; height: 265px;
    background:
      radial-gradient(ellipse 60% 90% at 50% 40%, rgba(255,255,255,0.35), transparent 70%),
      linear-gradient(180deg, var(--band-edge) 0, var(--band-bg) 12px, var(--band-bg) 100%);
  }
  .intro-text {
    position: absolute; left: 230px; top: 347px; width: 760px;
    font-size: 17px; line-height: 20.2px; letter-spacing: 2.3px;
  }

  .photo { position: absolute; top: 591px; height: 261px; }
  .photo-left {
    left: 223px; width: 370px;
    background:
      radial-gradient(ellipse 45% 40% at 48% 55%, var(--photo-left-warm), transparent 75%),
      radial-gradient(ellipse 80% 35% at 40% 100%, var(--photo-left-plate), transparent 70%),
      linear-gradient(160deg, var(--photo-left-dark) 0%, var(--photo-left-mid) 60%, var(--photo-left-dark) 100%);
  }
  .photo-right {
    left: 593px; width: 384px;
    background:
      radial-gradient(ellipse 35% 35% at 48% 60%, var(--photo-right-warm), transparent 75%),
      radial-gradient(ellipse 90% 30% at 55% 85%, var(--photo-right-plate), transparent 70%),
      radial-gradient(ellipse 40% 30% at 70% 15%, rgba(255,220,170,0.35), transparent 70%),
      linear-gradient(180deg, var(--photo-right-dark) 0%, var(--photo-right-mid) 55%, var(--photo-right-dark) 100%);
  }

  .footer-note {
    position: absolute; top: 976px; left: 422px; font-size: 12.5px; letter-spacing: 1.9px;
  }
  .footer-brand {
    position: absolute; left: 827px; top: 955px;
    display: flex; align-items: center; gap: 6px;
  }
  .footer-brand .brand-mark { width: 38px; height: 38px; border-radius: 4px; box-shadow: none; }
  .footer-brand .brand-name { font-size: 20px; letter-spacing: 0; margin-top: 6px; }
</style>
</head>
<body>
  <div class="column"></div>

  <div class="social" aria-label="Social links">
    <span></span><span></span><span></span><span></span>
  </div>

  <div class="brand">
    <div class="brand-mark"></div>
    <div class="brand-name">PanFolio</div>
  </div>

  <ul class="nav">
    <li class="home">home</li>
    <li class="about">about</li>
    <li class="contact">contact us</li>
    <li class="login">log in</li>
    <li class="logout">log out</li>
  </ul>

  <div class="search">
    <svg width="22" height="20" viewBox="0 0 22 20" aria-hidden="true">
      <circle cx="8" cy="8" r="5" fill="none" stroke="#111" stroke-width="2"/>
      <line x1="12" y1="11" x2="19" y2="16" stroke="#111" stroke-width="3" stroke-linecap="round"/>
    </svg>
  </div>

  <div class="intro-band"></div>
  <p class="intro-text">
    The PanFolio website will allow the publication of recipes of all types by<br>
    registered users. The website will be user friendly, easy to use and graphically<br>
    attractive. At the same time, it will be minimalistic as to not bloat the user with<br>
    too much options. The focus for the first version of the system is the publication<br>
    of recipes in a professional and ordered manner
  </p>

  <div class="photo photo-left" role="img" aria-label="Photo of a stacked burger with fried macaroni buns and salad on a white plate"></div>
  <div class="photo photo-right" role="img" aria-label="Photo of a gourmet burger topped with sprouts on a square plate"></div>

  <p class="footer-note">© 2014. All rights reserved.&nbsp; PanFolio Company</p>

  <div class="footer-brand">
    <div class="brand-mark"></div>
    <div class="brand-name">PanFolio</div>
  </div>
</body>
</html>
```